Breakfast Menu at a Bar and Grill

6" x 9" flyer
The attached powerpoint file contains slides with the text to be included in the front and back of the flyer. I will leave it to the designer to suggest color and background designs. Marlowe's Quiet Corner is a no frills dive bar with a blue color customer base. A simple breakfast theme will do.

Target Market(s)

Seniors and blue collar workers.

Font styles to use
Decorative

Colors

Designer to choose colors to be used in the design.

Requirements
Must have
• Our Logo (attached jpg) and the text in the attached PowerPoint file. Some kind of breakfast dish as the background. I will rely on the designers regards the font sizes.
Nice to have
• The background design should have a pic of a breakfast plate that matches one of the items on special...perhaps two pics?
Should not have
• pic that shows food that is not listed on the flyer.

```html
<!DOCTYPE html>
<html lang="en">
<head>
<meta charset="utf-8">
<title>Marlowe's Quiet Corner — Breakfast Specials Flyer</title>
<link rel="stylesheet" href="https://fonts.googleapis.com/css2?family=Montserrat:wght@800&family=Lobster&family=Playfair+Display:ital,wght@1,500&family=Lato:wght@400;900&display=swap">
<style>
  :root{
    --backdrop:#dcdcdc;
    --paper:#f7f7f7;
    --brand-red:#e84136;
    --banner-red:#c5161d;
    --ink:#111111;
    --white:#ffffff;
    --egg-light:#f6dc55;
    --egg-deep:#d9a61c;
    --plate:#efe9df;
    --berry:#9c1b25;
  }
  *{margin:0;padding:0;box-sizing:border-box}
  html,body{width:1200px;height:1200px;overflow:hidden;background:var(--backdrop)}
  body{position:relative;font-family:"Lato",sans-serif;color:var(--ink)}

  .page{position:absolute;overflow:hidden;box-shadow:0 2px 6px rgba(0,0,0,.18)}
  .page--front{left:62px;top:150px;width:527px;height:784px;background:var(--paper)}
  .page--back{left:613px;top:150px;width:538px;height:771px;background:var(--white)}

  .photo{position:absolute;left:0;top:0;display:block}

  .masthead{position:absolute;left:0;top:0;width:100%;text-align:center}
  .masthead__title{
    position:absolute;left:58px;top:42px;width:416px;height:38px;
    background:var(--banner-red);color:var(--white);
    font-family:"Montserrat",sans-serif;font-weight:800;font-size:30px;
    line-height:38px;letter-spacing:.5px;
  }
  .masthead__sub{
    position:absolute;left:112px;top:84px;width:304px;height:35px;
    background:var(--banner-red);color:var(--white);
    font-family:"Lobster",cursive;font-size:27px;line-height:35px;
  }
  .masthead__hours{
    position:absolute;left:0;top:130px;width:100%;
    font-family:"Lato",sans-serif;font-weight:900;font-size:35px;color:var(--white);
    -webkit-text-stroke:2px #2a2a2a;paint-order:stroke fill;
  }
  .masthead__days{
    position:absolute;left:0;top:170px;width:100%;
    font-size:17px;color:var(--brand-red);
    -webkit-text-stroke:2px var(--white);paint-order:stroke fill;
  }

  .offer{position:absolute;left:30px;top:243px;width:480px;text-align:center;font-size:11.5px;line-height:17px}
  .offer em{font-style:normal;color:var(--brand-red)}

  .menu-section{position:absolute;left:58px;width:412px}
  .menu-section h2{
    text-align:center;font-family:"Playfair Display",serif;font-style:italic;font-weight:500;
    color:var(--brand-red);font-size:28px;line-height:32px;margin-bottom:6px;
  }
  .menu-list{list-style:none}
  .menu-list li{display:flex;justify-content:space-between;font-size:17.5px;line-height:21px;text-transform:uppercase}
  .menu-list .price{color:var(--brand-red)}
  .section--traditional{top:290px}
  .section--traditional h2{padding-left:40px}
  .section--omelets{top:450px}
  .section--drinks{top:616px;left:60px}

  .back-brand{
    position:absolute;left:0;top:95px;width:100%;text-align:center;
    font-family:"Lato",sans-serif;font-weight:900;font-size:30px;color:var(--white);
  }
  .back-contact{
    position:absolute;left:0;top:224px;width:100%;text-align:center;
    font-size:19px;line-height:24px;color:var(--white);letter-spacing:.3px;
  }
</style>
</head>
<body>

<section class="page page--front" aria-label="Flyer front">
  <svg class="photo" width="527" height="250" viewBox="0 0 527 250" role="img" aria-label="Photo of a folded cheese omelet with herbs on a plate">
    <defs>
      <radialGradient id="omelet" cx="45%" cy="55%" r="70%">
        <stop offset="0" stop-color="var(--egg-light)"/>
        <stop offset=".6" stop-color="var(--egg-deep)"/>
        <stop offset="1" stop-color="#b98a3a"/>
      </radialGradient>
    </defs>
    <path fill="url(#omelet)" d="M0 0H527V235L515 240 505 228 492 244 470 232 455 238 440 226 420 236 400 230 380 238 360 228 340 236 320 230 300 240 280 228 260 236 240 224 220 234 200 228 180 238 160 226 140 234 120 228 100 236 80 226 60 234 40 228 20 236 0 230Z"/>
  </svg>

  <header class="masthead">
    <h1 class="masthead__title">MARLOWE'S QUIET CORNER</h1>
    <p class="masthead__sub">Breakfast Specials</p>
    <p class="masthead__hours">6AM – 11AM</p>
    <p class="masthead__days">7 Days A Week</p>
  </header>

  <p class="offer"><em>Free Breakfast</em> on Sunday with a two drink purchase.&nbsp; Monday through Saturday;<br>Purchase a breakfast special item with a two drink minimum and get one free.</p>

  <section class="menu-section section--traditional">
    <h2>Traditional Favorites</h2>
    <ul class="menu-list">
      <li><span>The 5-Star Breakfast</span><span class="price">$5.50</span></li>
      <li><span>Pancakes w/Bacon</span><span class="price">$5.50</span></li>
      <li><span>2 Eggs Bacon or Sausage</span><span class="price">$5.50</span></li>
      <li><span>3 Pancakes</span><span class="price">$4.00</span></li>
      <li><span>3 French Toast</span><span class="price">$4.00</span></li>
    </ul>
  </section>

  <section class="menu-section section--omelets">
    <h2>Omelets</h2>
    <ul class="menu-list">
      <li><span>California Omelet</span><span class="price">$6.00</span></li>
      <li><span>Green Chili Omelet</span><span class="price">$6.00</span></li>
      <li><span>Pueblo Omelet</span><span class="price">$6.00</span></li>
      <li><span>Spanish Omelet</span><span class="price">$6.00</span></li>
      <li><span>Basic Breakfast Omelet</span><span class="price">$6.00</span></li>
    </ul>
  </section>

  <section class="menu-section section--drinks">
    <h2>Drink Specials</h2>
    <ul class="menu-list">
      <li><span>Domestic Bottles</span><span class="price">$1.75</span></li>
      <li><span>Domestic Drafts</span><span class="price">$2.00</span></li>
      <li><span>Well Drinks</span><span class="price">$3.00</span></li>
      <li><span>Screwdrivers</span><span class="price">$3.00</span></li>
    </ul>
  </section>
</section>

<section class="page page--back" aria-label="Flyer back">
  <svg class="photo" width="538" height="771" viewBox="0 0 538 771">
    <defs>
      <radialGradient id="stack" cx="35%" cy="65%" r="65%">
        <stop offset="0" stop-color="var(--berry)"/>
        <stop offset=".35" stop-color="#d8a36a"/>
        <stop offset=".7" stop-color="var(--plate)"/>
        <stop offset="1" stop-color="#f8f5f0"/>
      </radialGradient>
    </defs>
    <rect y="330" width="538" height="441" fill="url(#stack)" role="img" aria-label="Photo of a stack of small pancakes topped with cherries, sauce and mint"/>
    <path fill="var(--brand-red)" d="M0 0H538V430L528 410 518 440 505 420 490 432 475 400 460 428 445 410 430 430 410 412 395 425 380 402 360 420 340 405 320 418 300 400 285 412 270 395 255 408 240 390 220 398 200 380 185 395 170 375 150 392 130 385 110 400 90 388 70 408 50 395 30 410 15 398 0 412Z"/>
  </svg>

  <p class="back-brand">Marlowe's Quiet Corner</p>
  <address class="back-contact" style="font-style:normal">
    4810 E JUNIPER MILL RD.<br>
    MESA, AZ 85205<br>
    480-555-0172
  </address>
</section>

</body>
</html>
```